Financial industry/Advisor business card

I'm a Financial Advisor starting my own investment company, Brantley Wealth Management. I currently use the 'Light Blue' color that's provided on the Cardwise web page, but I want something unique. I'd like to keep the color, but the design is up for grabs.

Industry/Entity Type

Business

Contact Information for Business Card

Brantley Wealth Management
Dean R. Brantley
President
5129 Willowgate Ln
Ste 240
Ashcombe Ford Pa 28406
555-372-6140-Office
555-372-6187-Fax
DBRANTLEY@BRANTWM.example

```html
<!DOCTYPE html>
<html lang="en">
<head>
<meta charset="utf-8">
<title>Brantley Wealth Management – Business Card</title>
<link rel="stylesheet" href="https://fonts.googleapis.com/css2?family=Mulish:wght@400;600;700&display=swap">
<style>
  :root {
    --navy: #0a6499;
    --sky: #6ecdf2;
    --paper: #ffffff;
    --backdrop: #e9ecef;
  }
  * { margin: 0; padding: 0; box-sizing: border-box; }
  html, body { width: 1200px; height: 1000px; overflow: hidden; }
  body {
    background: var(--backdrop);
    font-family: "Mulish", "Avenir", sans-serif;
    position: relative;
  }
  .card {
    position: absolute;
    width: 560px;
    height: 320px;
    background: var(--paper);
    overflow: hidden;
    box-shadow: 0 6px 18px rgba(0,0,0,0.18);
  }
  .card--front { left: 80px; top: 150px; }
  .card--back { left: 560px; top: 530px; }

  .wordmark {
    position: absolute;
    left: 0; right: 0; top: 50%;
    transform: translateY(-50%);
    text-align: center;
    color: var(--navy);
    font-weight: 600;
    letter-spacing: 0.04em;
    line-height: 1.2;
  }
  .wordmark__name { display: block; font-size: 23px; }
  .wordmark__tagline { display: block; font-size: 16px; }

  .block { position: absolute; }
  .block--sky { background: var(--sky); }
  .block--navy { background: var(--navy); }
  .back-accent { left: 62px; top: 22px; width: 240px; height: 206px; }
  .back-nameplate { left: 0; top: 56px; width: 286px; height: 150px; }
  .back-panel { left: 302px; top: 100px; width: 258px; height: 220px; }

  .person {
    position: absolute;
    left: 0; top: 100px; width: 286px;
    text-align: center;
    color: var(--paper);
  }
  .person__name { font-size: 20px; font-weight: 700; letter-spacing: 0.02em; }
  .person__title { font-size: 14px; font-weight: 600; margin-top: 2px; }

  .contact {
    position: absolute;
    left: 318px; top: 150px;
    color: var(--navy);
    font-size: 14px;
    font-style: normal;
    font-weight: 600;
    line-height: 22px;
    letter-spacing: 0.01em;
  }
  .contact__email { margin-top: 14px; font-size: 13px; letter-spacing: 0; }
</style>
</head>
<body>
  <section class="card card--front" aria-label="Card front">
    <h1 class="wordmark">
      <span class="wordmark__name">BRANTLEY</span>
      <span class="wordmark__tagline">WEALTH MANAGEMENT</span>
    </h1>
  </section>

  <section class="card card--back" aria-label="Card back">
    <div class="block block--sky back-accent"></div>
    <div class="block block--navy back-nameplate"></div>
    <div class="block block--sky back-panel"></div>
    <div class="person">
      <p class="person__name">Dean R. Brantley</p>
      <p class="person__title">President</p>
    </div>
    <address class="contact">
      <p>5129 Willowgate Ln Ste 240</p>
      <p>Ashcombe Ford, Pa 28406</p>
      <p>555-372-6140-Office</p>
      <p>555-372-6187-Fax</p>
      <p class="contact__email">DBRANTLEY@BRANTWM.example</p>
    </address>
  </section>
</body>
</html>
```